We require a business card that promotes our Electrical business. Things we would like included are;
1) our business name, Bright Path Electrical and Communication
2) Our Electrical licence, EC 73620
3) Our ABN, 41 297 506 183
4) Our website, www.korvanelectric.com.au
5) Our Email, info@korvanelectric.com.au
6) Our contact number, 0462 158 704
7) Our address, 57 Larkfield Rd West Dunmore Perth 6109
8) Our logo, I will attach this (can you please change it so the ackground is white not black)
9) Our colours are red and white and perhaps some black
10) Managing Director Tomasz Relhuvan
11) the back to say 'notes' and have some lines for writing

Target Market(s)

General

Industry/Entity Type

Electrical

Contact Information for Business Card

Include the colour white, black and red.

Font styles to use
Sans Serif

Requirements
Nice to have
• A thunder bolt or a power point or a cord or something electrical, cartoon image of a cartoon like electrical tradie

```html
<!DOCTYPE html>
<html lang="en">
<head>
<meta charset="utf-8">
<title>Bright Path Electrical and Communication — Business Card</title>
<link href="https://fonts.googleapis.com/css2?family=Montserrat:wght@400;500;600;700&display=swap" rel="stylesheet">
<style>
  :root {
    --red: #e3252f;
    --red-deep: #c81f28;
    --black: #111111;
    --white: #ffffff;
    --paper: #f4f4f4;
    --stage: #e6e3de;
    --ink-soft: #f3d9da;
  }
  html, body {
    margin: 0;
    padding: 0;
    width: 1200px;
    height: 780px;
    overflow: hidden;
    background: var(--stage);
    font-family: "Montserrat", Arial, sans-serif;
  }
  .canvas {
    position: relative;
    width: 1200px;
    height: 780px;
  }
  .card {
    position: absolute;
    top: 235px;
    width: 540px;
    height: 310px;
    border-radius: 18px;
    overflow: hidden;
    box-shadow: 0 10px 28px rgba(0,0,0,0.18);
  }
  .card--front { left: 40px; }
  .card--back { left: 620px; }
  .card__bg {
    position: absolute;
    inset: 0;
    width: 540px;
    height: 310px;
  }
  .text { position: absolute; margin: 0; white-space: nowrap; }

  /* Front */
  .brand-name {
    left: 26px; top: 34px;
    font-size: 29px; font-weight: 700;
    color: var(--red); letter-spacing: 0.2px;
  }
  .brand-sub {
    left: 92px; top: 72px;
    font-size: 20px; font-weight: 600;
    color: var(--red);
  }
  .person-name {
    left: 26px; top: 206px;
    font-size: 21px; font-weight: 700;
    color: var(--white);
  }
  .person-role {
    left: 26px; top: 234px;
    font-size: 13px; font-weight: 500;
    color: var(--white);
  }
  .divider {
    position: absolute;
    left: 238px; top: 176px;
    width: 1px; height: 78px;
    background: rgba(255,255,255,0.7);
  }
  .contacts {
    position: absolute;
    left: 252px; top: 174px;
    margin: 0; padding: 0;
    list-style: none;
    color: var(--white);
    font-size: 11.5px; font-weight: 500;
  }
  .contacts li {
    display: flex; align-items: center;
    height: 20px;
  }
  .contacts svg { width: 12px; height: 12px; margin-right: 7px; flex: none; }
  .address {
    left: 0; width: 540px; top: 279px;
    text-align: center;
    font-size: 13px; font-weight: 500;
    color: var(--white);
  }

  /* Back */
  .notes-title {
    left: 300px; top: 34px;
    font-size: 26px; font-weight: 500;
    color: var(--red);
  }
  .back-mark {
    left: 250px; top: 120px;
    font-size: 40px; font-weight: 700;
    color: var(--ink-soft);
    opacity: 0.6;
  }
  .licence {
    left: 24px; top: 268px;
    font-size: 14px; font-weight: 500;
    color: var(--black);
  }
</style>
</head>
<body>
<main class="canvas">

  <section class="card card--front" aria-label="Business card front">
    <svg class="card__bg" viewBox="0 0 540 310" aria-hidden="true">
      <defs>
        <linearGradient id="whiteFace" x1="0" y1="0" x2="1" y2="1">
          <stop offset="0" stop-color="#ffffff"/>
          <stop offset="1" stop-color="#e9e9e9"/>
        </linearGradient>
        <linearGradient id="redFace" x1="0" y1="0" x2="1" y2="1">
          <stop offset="0" stop-color="#ee2b35"/>
          <stop offset="1" stop-color="#d6222b"/>
        </linearGradient>
      </defs>
      <rect width="540" height="310" fill="url(#redFace)"/>
      <rect y="268" width="540" height="42" fill="var(--black)"/>
      <path d="M0 195 C240 182 372 112 404 0 H418 C390 124 250 198 0 206 Z" fill="var(--black)"/>
      <path d="M0 0 H404 C372 112 240 182 0 195 Z" fill="url(#whiteFace)"/>
    </svg>

    <h1 class="text brand-name">Bright Path Electrical</h1>
    <p class="text brand-sub">and Communication</p>

    <p class="text person-name">Tomasz Relhuvan</p>
    <p class="text person-role">Managing Director</p>
    <span class="divider"></span>

    <ul class="contacts">
      <li>
        <svg viewBox="0 0 12 12" aria-hidden="true"><path d="M2.5 1 L4.5 1 L5.2 3.5 L4 4.4 C4.6 5.8 6.2 7.4 7.6 8 L8.5 6.8 L11 7.5 L11 9.5 C11 10.4 10.3 11 9.5 11 C5 10.6 1.4 7 1 2.5 C1 1.7 1.6 1 2.5 1 Z" fill="var(--white)"/></svg>
        0462 158 704
      </li>
      <li>
        <svg viewBox="0 0 12 12" aria-hidden="true"><rect x="0.8" y="2.5" width="10.4" height="7" fill="none" stroke="var(--white)" stroke-width="1.2"/><path d="M1 3 L6 6.8 L11 3" fill="none" stroke="var(--white)" stroke-width="1.2"/></svg>
        info@korvanelectric.com.au
      </li>
      <li>
        <svg viewBox="0 0 12 12" aria-hidden="true"><circle cx="6" cy="6" r="5" fill="none" stroke="var(--white)" stroke-width="1.1"/><ellipse cx="6" cy="6" rx="2.2" ry="5" fill="none" stroke="var(--white)" stroke-width="1"/><path d="M1 6 H11" stroke="var(--white)" stroke-width="1"/></svg>
        www.korvanelectric.com.au
      </li>
      <li>ABN 41 297 506 183</li>
    </ul>

    <p class="text address">57 Larkfield Rd West Dunmore Perth 6109</p>
  </section>

  <section class="card card--back" aria-label="Business card back">
    <svg class="card__bg" viewBox="0 0 540 310" aria-hidden="true">
      <defs>
        <linearGradient id="whiteBack" x1="0" y1="0" x2="1" y2="1">
          <stop offset="0" stop-color="#ffffff"/>
          <stop offset="1" stop-color="#e6e6e6"/>
        </linearGradient>
      </defs>
      <rect width="540" height="310" fill="var(--red-deep)"/>
      <path d="M0 108 C210 128 380 210 446 310 H432 C366 218 204 140 0 120 Z" fill="var(--black)"/>
      <path d="M0 0 H540 V310 H446 C380 210 210 128 0 108 Z" fill="url(#whiteBack)"/>
      <g stroke="#333" stroke-width="0.8">
        <line x1="190" y1="112" x2="510" y2="112"/>
        <line x1="250" y1="160" x2="510" y2="160"/>
        <line x1="318" y1="208" x2="510" y2="208"/>
      </g>
    </svg>

    <p class="text back-mark" aria-hidden="true">Bright Path</p>
    <h2 class="text notes-title">Notes</h2>
    <p class="text licence">Electrical licence&nbsp; EC 73620</p>
  </section>

</main>
</body>
</html>
```